Harborlight Willow Home Care Business Cards

We are looking to create double sided, sleek business cards for our new Home Health Care Agency, Harborlight Willow Home Care, located in NJ. We want to appear established, professional and at the same time, stand out with a creative and original flair. It should have a luxurious, exclusive feel to it.
The theme colors from our logo should be incorporated into the project.

Our Logo is attached.

Information to be included on the business cards:

Insert Phone Icon: (555)-204-7390
Insert Website Icon: hwhcpx.example
Insert E-mail Icon: info@hwhcpx.example

Follow us on Social Media!
Insert Facebook Icon: (I will provide the link at a later time)
Insert Instagram Icon (I will provide the link at a later time)

In regard to location, we service the areas of: Bayville
Beachwood
Brick
Deal
Howell
Island Heights
Jackson
Lakehurst
Lakewood
Manchester Township
Point Pleasant Beach
Roosevelt
Long Branch
Toms River

All all it's neighboring areas.

However, that can take up a lot of room...therefore, I had in mind to use the backside of the card to have a MAP with all these areas marked on there...in addition to listing these service locations below the map.

We want the card to appear lively and vibrant.

Please note: I will provide the potential winner with the contact's name later on in the process.

A sample idea is attached below as well.

Use your creative juices!

Good luck!

• A map of our service areas on the back of the double sided card.
Sleek design
Our logo (refer to attachment below)

```html
<!DOCTYPE html>
<html lang="en">
<head>
<meta charset="utf-8">
<title>Harborlight Willow Home Care – Business Cards</title>
<link rel="stylesheet" href="https://fonts.googleapis.com/css2?family=Montserrat:wght@600;700&display=swap">
<style>
  :root {
    --navy: #1b3f6e;
    --navy-soft: #5d7596;
    --green: #7dc242;
    --white: #ffffff;
    --stage: #a9a9a9;
    --land: #eeeeee;
    --land-shade: #d9dee6;
  }
  * { margin: 0; padding: 0; box-sizing: border-box; }
  html, body { width: 1200px; height: 1000px; overflow: hidden; background: var(--stage); }
  body { position: relative; font-family: "Montserrat", Arial, sans-serif; }

  .card { position: absolute; left: 180px; width: 840px; height: 480px; overflow: hidden; }
  .card-front { top: 12px; background: var(--white); }
  .card-back { top: 508px; background: var(--navy); }

  .contact-tab {
    position: absolute; left: 400px; top: 0; width: 52px; height: 258px;
    background: var(--navy); border-radius: 0 0 26px 26px;
  }
  .bottom-tab {
    position: absolute; left: 217px; bottom: 0; width: 408px; height: 20px;
    background: var(--navy); border-radius: 20px 20px 0 0;
  }

  .brand { position: absolute; left: 70px; top: 160px; width: 276px; text-align: center; }
  .brand-dot {
    width: 96px; height: 96px; border-radius: 50%; background: var(--navy);
    margin: 0 auto 22px;
  }
  .brand-name {
    color: var(--navy); font-weight: 700; font-size: 19px; line-height: 1.15;
    letter-spacing: 0.3px; text-transform: uppercase;
  }
  .brand-tagline {
    margin-top: 6px; color: var(--navy); font-weight: 600; font-size: 8.5px;
    letter-spacing: 1.6px; text-transform: uppercase;
  }

  .contact-list { position: absolute; left: 405px; top: 0; list-style: none; }
  .contact-item { position: absolute; left: 0; display: flex; align-items: center; white-space: nowrap; }
  .contact-item .icon {
    width: 40px; height: 40px; border-radius: 50%; flex: none;
    display: flex; align-items: center; justify-content: center;
  }
  .icon-light { background: #e8ecf2; }
  .icon-dark { background: var(--navy); }
  .contact-item .label {
    margin-left: 26px; color: var(--navy); font-weight: 700; font-size: 27px;
  }

  .service-map {
    position: absolute; inset: 0;
    background: linear-gradient(122deg,
      var(--land) 0%, var(--land) 26%, var(--land-shade) 38%,
      var(--navy-soft) 46%, var(--navy) 54%);
  }
  .services { position: absolute; right: 40px; top: 60px; text-align: right; }
  .services-title {
    color: var(--green); font-weight: 700; font-size: 32px; line-height: 1.15;
    margin-right: 10px;
  }
  .services-list {
    margin-top: 22px; color: var(--white); font-weight: 700; font-size: 28.5px;
    line-height: 33.5px; letter-spacing: -0.2px;
  }
</style>
</head>
<body>

<section class="card card-front">
  <div class="contact-tab"></div>
  <div class="bottom-tab"></div>

  <div class="brand">
    <div class="brand-dot"></div>
    <div class="brand-name">Harborlight Willow Home Care</div>
    <div class="brand-tagline">Trusted care from people nearby</div>
  </div>

  <ul class="contact-list">
    <li class="contact-item" style="top:58px">
      <span class="icon icon-light">
        <svg width="16" height="24" viewBox="0 0 16 24"><rect x="1" y="1" width="14" height="22" rx="2.5" fill="none" stroke="#1b3f6e" stroke-width="2"/><circle cx="8" cy="19" r="1.4" fill="#1b3f6e"/></svg>
      </span>
      <span class="label">(555)-204-7390</span>
    </li>
    <li class="contact-item" style="top:128px">
      <span class="icon icon-light">
        <svg width="26" height="26" viewBox="0 0 26 26" fill="none" stroke="#1b3f6e" stroke-width="1.8"><circle cx="13" cy="13" r="11"/><ellipse cx="13" cy="13" rx="5" ry="11"/><line x1="2" y1="13" x2="24" y2="13"/></svg>
      </span>
      <span class="label">hwhcpx.example</span>
    </li>
    <li class="contact-item" style="top:198px">
      <span class="icon icon-light">
        <svg width="26" height="18" viewBox="0 0 26 18" fill="none" stroke="#1b3f6e" stroke-width="1.8"><rect x="1" y="1" width="24" height="16" rx="1.5"/><polyline points="1,1 13,10 25,1"/></svg>
      </span>
      <span class="label">info@hwhcpx.example</span>
    </li>
    <li class="contact-item" style="top:296px">
      <span class="icon icon-dark"></span>
      <span class="label">friendsnet.example/user</span>
    </li>
    <li class="contact-item" style="top:372px">
      <span class="icon icon-dark"></span>
      <span class="label">snapgram.example/user</span>
    </li>
  </ul>
</section>

<section class="card card-back">
  <div class="service-map" role="img" aria-label="Map of the New Jersey shore, grey land meeting the navy sea, with a marker on each service area"></div>
  <div class="services">
    <h2 class="services-title">Our Services<br>Available at</h2>
    <p class="services-list">
      Bayville,<br>
      Beachwood,<br>
      Brick, Deal, Howell,<br>
      Island Heights Jackson,<br>
      Lakehurst, Lakewood,<br>
      Manchester Township<br>
      Point Pleasant Beach,<br>
      Roosevelt, Long Branch,<br>
      Toms River
    </p>
  </div>
</section>

</body>
</html>
```